PELDRAX Business Cards

We require a business card for our company that provides IT consulting services. We already have a logo that needs to be used on the card. We want a clean professional looking design that incorporates our colours. Our main focus is providing managed services to business, which involves us looking after all of their IT requirements including managing servers/networks, projects, and procurement.

Industry/Entity Type

Information Technology

Requirements
Must have
• our logo, contact information, name, title, phone numbers

```html
<!DOCTYPE html>
<html lang="en">
<head>
<meta charset="utf-8">
<title>PELDRAX Business Cards</title>
<link rel="stylesheet" href="https://fonts.googleapis.com/css2?family=Roboto:wght@400;500;700&display=swap">
<style>
  :root {
    --backdrop: #3a3a3c;
    --slate: #4f5456;
    --brand-blue: #1595cf;
    --paper: #f1f1f1;
    --white: #ffffff;
    --url-grey: #555a5c;
  }
  * { box-sizing: border-box; margin: 0; padding: 0; }
  html, body {
    width: 1200px; height: 960px; overflow: hidden;
    background: var(--backdrop);
    font-family: "Roboto", Arial, sans-serif;
  }
  .canvas { position: relative; width: 1200px; height: 960px; }
  .card {
    position: absolute; width: 600px; height: 342px; overflow: hidden;
    box-shadow: 0 3px 8px rgba(0,0,0,0.45);
  }
  .card-front { left: 314px; top: 113px; background: var(--brand-blue); }
  .card-back { left: 311px; top: 472px; background: var(--paper); }

  .slate-panel {
    position: absolute; left: 0; top: 0; bottom: 0;
    width: 190px; background: var(--slate);
  }
  .identity {
    position: absolute; right: 36px; top: 50px; text-align: right; color: var(--white);
  }
  .person-name { font-size: 21px; font-weight: 700; letter-spacing: 0.3px; line-height: 24px; }
  .person-title { font-size: 14px; font-weight: 500; line-height: 18px; }

  .address {
    position: absolute; right: 36px; top: 168px; text-align: right;
    color: var(--white); font-size: 14px; line-height: 18px;
  }
  .contact-list {
    position: absolute; right: 38px; top: 215px; list-style: none;
    color: var(--white); font-size: 14px;
  }
  .contact-list li {
    display: flex; justify-content: flex-end; align-items: center;
    height: 19.5px; gap: 8px;
  }
  .contact-list svg { width: 14px; height: 14px; fill: var(--white); flex: none; }

  .wordmark {
    position: absolute; left: 143px; top: 148px;
    display: flex; align-items: center; gap: 12px;
  }
  .wordmark-dot { width: 44px; height: 44px; border-radius: 50%; background: var(--brand-blue); }
  .wordmark-name {
    font-size: 54px; font-weight: 500; color: var(--brand-blue);
    letter-spacing: 2px; line-height: 1;
  }
  .back-url {
    position: absolute; left: 0; right: 0; top: 298px; text-align: center;
    font-size: 14px; color: var(--url-grey); letter-spacing: 5px;
  }
</style>
</head>
<body>
<main class="canvas">
  <section class="card card-front">
    <div class="slate-panel"></div>
    <div class="identity">
      <p class="person-name">MARCUS HALE</p>
      <p class="person-title">CEO/FOUNDER</p>
    </div>
    <address class="address" style="font-style:normal">
      4120 Larkspur Court<br>Fairbanks, Alaska 99712
    </address>
    <ul class="contact-list">
      <li>555 204 7816
        <svg viewBox="0 0 16 16"><path d="M3.5 1l2.5 3-1.5 2a9 9 0 0 0 5 5l2-1.5 3 2.5-1.5 2.5C7 14 2 9 1 2.5z"/></svg></li>
      <li>555 319 6402
        <svg viewBox="0 0 16 16"><path d="M4 0h8v16H4zM5.5 2v10h5V2zM7 13.2v1.3h2v-1.3z" fill-rule="evenodd"/></svg></li>
      <li>555 872 0593
        <svg viewBox="0 0 16 16"><path d="M4 1h8v4H4zM1 6h14v7h-2v2H3v-2H1zM4.5 10v3.5h7V10z" fill-rule="evenodd"/></svg></li>
      <li>marcus@peldrax.com
        <svg viewBox="0 0 16 16"><path d="M1 3h14v10H1zM2.2 4.3v.4L8 9l5.8-4.3v-.4zM2.2 6.1v5.7h11.6V6.1L8 10.4z" fill-rule="evenodd"/></svg></li>
      <li>www.peldrax.com
        <svg viewBox="0 0 16 16"><circle cx="8" cy="8" r="7"/><path d="M5 4c2 0 2 2 4 2s0 3-2 3-1 3-3 2-2-4 1-7zM11 10c1 0 2 1 1 2s-2 0-1-2z" fill="#1595cf"/></svg></li>
    </ul>
  </section>

  <section class="card card-back">
    <div class="wordmark">
      <span class="wordmark-dot"></span>
      <span class="wordmark-name">PELDRAX</span>
    </div>
    <p class="back-url">www.peldrax.com</p>
  </section>
</main>
</body>
</html>
```